Hardware Brand Packaging Design Project

We require a design for packaging for products in the retail hardware range. Initially this will be for a set of header cards for abrasive sanding discs but we plan to add other items to the range so we are looking for a range of brand elements that can be extended to other types of packaging.
The brand name is "Gleam Ridge" and we are looking for a black or dark grey background with a subtle fine pattern to break up the solid colour. This part of the design needs to be 'expandable' so that it can be used on different pack sizes as we increase the range. Two highlight or complimentary colours will add a bit of impact and become part of the brand style.
For printing purposes we have allowed for 4 colour process plus two spot colours and we have attached one of the header card dielines as a guide.
Target Market(s)
Home owners of both gender in the 25 to 55 age range
Industry/Entity Type
Printing
Requirements
Must have
- *The brand name "Gleam Ridge" should appear in the top left hand corner and we had in mind that the word would be a shiny metal / chrome appearance in could be in the shape of a shield or spear point but are open to any other suggestions.The word can be on one line or one above the other.
*Between the bottom of the hanger hole and the edge of the card is the words ABRASIVES & ACCESSORIES
*We want a performance guarantee device circle / seal or other in the bottom left quartile of the front facing panel. Circle device on attachment shows approx position.
* The right hand 25mm of the card is to be devoted to specific information about the product in the pack. This will be done by an adhered over-sticker ( see attached die-line No 2 )
* 3 line address panel or rear of card - QRT Abrasives, 47 Lane, West Auckland, New Zealand.
* Also somewhere on rear panel "Cut, Quality Checked & Packed in New Zealand from imported materials."
Nice to have
- It would be good, but not essential, to see a rough mock-up of how this design would transfer across to a box approx 80mm across the front, 100mm deep and 250mm high.

```html
<!DOCTYPE html>
<html lang="en">
<head>
<meta charset="utf-8">
<title>Gleam Ridge – Abrasives Header Card</title>
<link rel="stylesheet" href="https://fonts.googleapis.com/css2?family=Oswald:wght@500;600&family=Arimo:wght@400&display=swap">
<style>
  :root {
    --page: #ffffff;
    --card-black: #141414;
    --brand-red: #5a0000;
    --ink-white: #ffffff;
    --seal-gold: #b38a32;
    --seal-ink: #141414;
    --fine-print: #2e0000;
  }
  html, body {
    margin: 0;
    width: 1200px;
    height: 900px;
    overflow: hidden;
    background: var(--page);
  }
  .header-card {
    position: relative;
    width: 1200px;
    height: 900px;
    overflow: hidden;
  }
  .dieline {
    position: absolute;
    inset: 0;
  }
  .flipped {
    position: absolute;
    transform: rotate(180deg);
  }
  .brand-name {
    position: absolute;
    margin: 0;
    font-family: "Oswald", sans-serif;
    font-weight: 600;
    font-size: 52px;
    line-height: 0.96;
    color: var(--ink-white);
    text-transform: uppercase;
    display: flex;
    align-items: flex-end;
    gap: 10px;
  }
  .brand-name .brand-square {
    width: 14px;
    height: 14px;
    background: var(--brand-red);
    margin-bottom: 8px;
  }
  .brand-name--back { left: 165px; top: 52px; width: 150px; }
  .brand-name--front { left: 182px; top: 500px; }
  .address-panel {
    left: 145px;
    top: 196px;
    width: 585px;
    height: 92px;
    margin: 0;
    font-family: "Arimo", sans-serif;
    font-size: 40px;
    line-height: 1.08;
    color: var(--ink-white);
    font-style: normal;
    text-align: left;
  }
  .origin-note {
    left: 140px;
    top: 340px;
    width: 210px;
    height: 96px;
    margin: 0;
    font-family: "Arimo", sans-serif;
    font-size: 17px;
    line-height: 1.9;
    color: var(--fine-print);
    text-align: left;
  }
  .range-title {
    position: absolute;
    left: 150px;
    top: 651px;
    margin: 0;
    font-family: "Oswald", sans-serif;
    font-weight: 500;
    font-size: 76px;
    line-height: 1;
    letter-spacing: -0.5px;
    color: var(--ink-white);
    text-transform: uppercase;
    white-space: nowrap;
  }
  .quality-seal {
    position: absolute;
    left: 175px;
    top: 755px;
    width: 146px;
    height: 104px;
    border-radius: 50%;
    background: var(--seal-gold);
    display: flex;
    flex-direction: column;
    align-items: center;
    justify-content: center;
    font-family: "Oswald", sans-serif;
    font-weight: 600;
    font-size: 29px;
    line-height: 1;
    color: var(--seal-ink);
    text-transform: uppercase;
  }
</style>
</head>
<body>
<main class="header-card">
  <svg class="dieline" width="1200" height="900" viewBox="0 0 1200 900" aria-hidden="true">
    <rect class="card-body" x="135" y="5" width="968" height="892" rx="26" fill="var(--card-black)"/>
    <rect class="band-back" x="135" y="193" width="968" height="257" fill="var(--brand-red)"/>
    <rect class="band-front" x="135" y="660" width="968" height="70" fill="var(--brand-red)"/>
    <circle class="cutout-top" cx="620" cy="-350" r="478" fill="var(--page)"/>
    <circle class="cutout-bottom" cx="620" cy="1247" r="478" fill="var(--page)"/>
    <path class="hanger-hole" fill="var(--page)" d="
      M355,450 L450,300 Q458,290 472,290 L710,290 A27,27 0 0 1 712,344
      C690,345 660,338 650,352 C640,372 600,375 595,355 C590,335 575,335 560,340
      C540,345 530,345 520,335 C505,315 485,318 475,335 L430,410 Q420,430 432,446
      L432,454 Q420,470 430,490 L475,565 C485,582 505,585 520,565
      C530,555 540,555 560,560 C575,565 590,565 595,545 C600,525 640,528 650,548
      C660,562 690,555 712,556 A27,27 0 0 1 710,610 L472,610 Q458,610 450,600 Z"/>
  </svg>

  <h2 class="brand-name brand-name--back flipped"><span>Gleam<br>Ridge</span><span class="brand-square"></span></h2>

  <address class="address-panel flipped">QRT Abrasives, 47 Lane,<br>West Auckland, New Zealand.</address>

  <p class="origin-note flipped">Cut, Quality Checked<br>&amp; Packed in New Zealand<br>from imported materials.</p>

  <h1 class="brand-name brand-name--front"><span>Gleam<br>Ridge</span><span class="brand-square"></span></h1>

  <p class="range-title">Abrasives &amp; Accessories</p>

  <div class="quality-seal"><span>Quality</span><span>Assured</span></div>
</main>
</body>
</html>
```